Website homepage rework for women's travel website

I have a homepage (http://www.ladies-far-afield.example) that I'm 50% happy with but don't want to completely overhaul. I'd like to retain a similar look but upgrade it to something a bit more modern and less old-fashioned. The basic sense of the site is empowering, self-confident, fun and adventurous - but female and over 40.

A number of the elements on the page have to be redesigned, a few can be tweaked, and a few left alone. See the rest of the brief for further information.

Target Market(s)

women over 40 who like to travel

Industry/Entity Type

Travel

Number of Pages Required

1 page

Font styles to use
Other font styles liked:
• see my brief

Requirements
Must have
• - size - the page must be significantly wider
• - the only font I MUST keep is Raleway (as in the tagline) and possibly the font of the site name (Ladies Far Afield). Both of those work for me. There are too many fonts on the page, however, and that needs to be unified.
• - the rectangles I click to get inside the site have to change to something more modern, possibly square - they do not have to be separated into two columns as they are now, nor do they need the titles (toolkit etc)
• - I like the background image of the header - but it needs to be wider of course - also keep in mind the aspect - it has to fit into the smaller inside pages, whose size will not change
• - at the end of the project I need to receive the separate elements of the design so I can eventually make a change myself if needed ie. replace my own photo, for example
Nice to have
• - the three photos need to change to something more eye-popping - or something else should take their place to fill the space
Should not have
• I do not want a full, original redesign. I want my readers to still feel as though they are on the same site - same header, mostly same fonts.

```html
<!DOCTYPE html>
<html lang="en">
<head>
<meta charset="utf-8">
<title>Ladies Far Afield – For women who travel smart, safe + solo</title>
<link href="https://fonts.googleapis.com/css2?family=Raleway:wght@400;500;600;700;800&display=swap" rel="stylesheet">
<style>
:root{
  --red:#b3191e;
  --red-dark:#8e1115;
  --nav:#3a2f24;
  --band:#2d2926;
  --orange:#e8901a;
  --ink:#333333;
  --muted:#666666;
  --grey-bg:#efefef;
  --footer-bg:#f0f0f0;
  --white:#ffffff;
}
*{box-sizing:border-box;margin:0;padding:0}
html,body{width:1200px;height:2624px;overflow:hidden}
body{position:relative;background:var(--white);font-family:'Raleway',sans-serif;color:var(--ink)}
.abs{position:absolute}

/* top bar */
.topbar{left:0;top:0;width:1200px;height:74px;background:var(--white)}
.contact-item{top:16px;display:flex;gap:12px;align-items:flex-start}
.contact-item .ico{width:36px;height:36px;border:2px solid var(--red);border-radius:50%;display:flex;align-items:center;justify-content:center}
.contact-item .label{color:var(--red);font-size:14px;font-weight:600;line-height:18px}
.contact-item .value{color:var(--muted);font-size:12px;line-height:18px}
.search{left:920px;top:17px;width:191px;height:39px;border:2px solid var(--red);border-radius:8px;display:flex;align-items:center;justify-content:space-between;padding:0 14px;color:#999;font-size:12px}

/* nav */
.nav{left:0;top:74px;width:1200px;height:80px;background:var(--nav)}
.nav-link{top:106px;color:var(--white);font-size:13px;font-weight:700;letter-spacing:.2px;display:flex;align-items:center;gap:8px}
.brand{left:484px;top:79px;width:280px;height:70px;background:#5a4c3e;display:flex;flex-direction:column;align-items:center;justify-content:center;gap:4px}
.brand-name{color:var(--white);font-size:25px;font-weight:600;display:flex;align-items:center;gap:8px}
.brand-name .sq{width:12px;height:12px;background:var(--red)}
.brand-tag{color:#e6ddd3;font-size:12px}

/* hero */
.hero{left:0;top:154px;width:1200px;height:432px;background:linear-gradient(100deg,#c8a050 0%,#e8b030 35%,#d98a28 60%,#8c5a30 85%,#5c3a22 100%)}
.hero-card{left:500px;top:255px;width:613px;height:186px;background:rgba(80,60,40,.55);border:1px solid rgba(255,255,255,.6);border-radius:8px;padding:14px 20px;text-align:right}
.hero-card h1{color:var(--white);font-size:40px;font-weight:700;line-height:52px}
.btn-ghost{display:inline-block;margin-top:20px;border:1px solid var(--white);border-radius:8px;color:var(--white);font-size:13px;font-weight:700;padding:10px 18px}
.dots{left:576px;top:560px;display:flex;gap:4px}
.dots span{width:14px;height:14px;border-radius:50%;background:var(--white);border:2px solid #ddd}
.dots span.on{border-color:var(--red)}

/* intro */
.intro{left:87px;top:626px;width:1030px}
.intro h2{font-size:32px;font-weight:600;line-height:38px;color:#2b2b2b}
.intro ul{list-style:none;margin-top:22px;margin-left:30px}
.intro li{font-size:16px;line-height:31px;position:relative;padding-left:20px}
.intro li::before{content:"";position:absolute;left:0;top:11px;width:6px;height:9px;background:var(--red)}

/* cta band */
.cta{left:0;top:840px;width:1200px;height:84px;background:var(--band);display:flex;align-items:center;justify-content:center;color:var(--orange);font-size:27px;font-weight:600}
.cta u{margin:0 8px}

/* sections */
.toolkit{left:0;top:924px;width:1200px;height:414px;background:var(--grey-bg)}
.section-title{left:0;width:1200px;text-align:center;font-size:26px;font-weight:500;color:#333;letter-spacing:.5px}
.cards{left:87px;width:1026px;display:flex;gap:21px}
.card{width:241px;height:222px;position:relative;box-shadow:0 4px 5px rgba(0,0,0,.3);overflow:hidden}
.card-head{height:72px;background:linear-gradient(#c21d22,var(--red-dark));padding:10px 12px;color:var(--white)}
.card-head h3{font-size:19px;font-weight:700;line-height:20px;text-transform:uppercase}
.card-head p{font-size:13px;line-height:17px;margin-top:3px}
.card-photo{height:150px}
.card-link{position:absolute;left:0;right:0;top:130px;text-align:center;color:var(--white);font-size:11px;text-decoration:underline}
.arrow{width:24px;height:24px;border-radius:50%;background:#333;display:flex;align-items:center;justify-content:center}

/* solo travel */
.solo-bg{left:87px;top:1768px;width:430px;height:392px;background:#f3f3f3}
.solo-panel{left:91px;top:1780px;width:416px;height:371px;border:2px solid #999;background:#ededed;padding:66px 18px 0 18px}
.solo-panel h2{color:var(--red);font-size:25px;font-weight:600}
.solo-panel p{font-size:12px;line-height:21px;color:var(--muted);margin-top:12px}
.btn-outline{display:inline-block;margin-top:28px;border:1px solid #555;color:#333;font-size:12px;font-weight:700;padding:11px 16px}
.solo-photo{left:516px;top:1767px;width:597px;height:398px;background:radial-gradient(circle at 55% 45%,#4a4642,#262422 75%);box-shadow:0 3px 6px rgba(0,0,0,.4)}
.solo-frame{left:530px;top:1779px;width:569px;height:374px;border:2px solid var(--white)}

/* footer */
.footer{left:0;top:2244px;width:1200px;height:338px;background:var(--footer-bg)}
.foot-h{top:2296px;font-size:18px;font-weight:700;color:#333}
.foot-brand{left:87px;top:2338px;width:260px;height:54px;display:flex;flex-direction:column;justify-content:center}
.foot-brand .name{color:var(--red);font-size:24px;font-weight:600}
.foot-brand .tag{color:#444;font-size:12px}
.socials{left:87px;top:2460px;display:flex;gap:10px}
.socials span{width:40px;height:40px;border:1.5px solid var(--orange);display:flex;align-items:center;justify-content:center}
.socials span i{width:12px;height:12px;background:var(--red);display:block}
.quick{left:453px;top:2334px;list-style:none}
.quick li{font-size:12px;line-height:34px;color:#444;display:flex;align-items:center;gap:18px}
.quick li::before{content:"";border-left:5px solid #333;border-top:4px solid transparent;border-bottom:4px solid transparent}
.field{border:1px solid #999;background:#f4f4f4;font-size:11px;color:#555;padding:0 10px;display:flex;align-items:center}
.send{left:705px;top:2494px;width:75px;height:35px;background:#c90d12;color:var(--white);font-size:12px;font-weight:700;display:flex;align-items:center;justify-content:center}
.bottom{left:0;top:2582px;width:1200px;height:42px;background:#3a3a3a;color:#ddd;font-size:12px;display:flex;align-items:center;justify-content:center}
</style>
</head>
<body>

<header>
  <div class="abs topbar"></div>
  <div class="abs contact-item" style="left:87px">
    <div class="ico"><svg width="16" height="16" viewBox="0 0 24 24"><path d="M6.6 10.8a15 15 0 0 0 6.6 6.6l2.2-2.2a1 1 0 0 1 1-.25 11.4 11.4 0 0 0 3.6.57 1 1 0 0 1 1 1V20a1 1 0 0 1-1 1A17 17 0 0 1 3 4a1 1 0 0 1 1-1h3.5a1 1 0 0 1 1 1c0 1.25.2 2.45.57 3.57a1 1 0 0 1-.25 1z" fill="#b3191e"/></svg></div>
    <div><div class="label">CALL US</div><div class="value">555-014-2207</div></div>
  </div>
  <div class="abs contact-item" style="left:240px">
    <div class="ico"><svg width="16" height="14" viewBox="0 0 24 20"><rect x="1" y="2" width="22" height="16" rx="2" fill="#b3191e"/><path d="M2 4l10 7 10-7" stroke="#fff" stroke-width="2" fill="none"/></svg></div>
    <div><div class="label">E-MAIL US</div><div class="value">info@ladiesfarafield.example</div></div>
  </div>
  <div class="abs search"><span>search...</span><svg width="15" height="15" viewBox="0 0 24 24"><circle cx="10" cy="10" r="7" stroke="#333" stroke-width="3" fill="none"/><path d="M15 15l6 6" stroke="#333" stroke-width="3"/></svg></div>

  <nav>
    <div class="abs nav"></div>
    <div class="abs nav-link" style="left:87px">START HERE</div>
    <div class="abs nav-link" style="left:215px">ABOUT</div>
    <div class="abs nav-link" style="left:313px">TRAVEL RESOURCES <svg width="9" height="6" viewBox="0 0 9 6"><path d="M1 1l3.5 3.5L8 1" stroke="#fff" fill="none" stroke-width="1.4"/></svg></div>
    <div class="abs brand"><div class="brand-name"><span class="sq"></span>Ladies Far Afield</div><div class="brand-tag">For women who travel smart, safe + solo</div></div>
    <div class="abs nav-link" style="left:796px">BLOG</div>
    <div class="abs nav-link" style="left:887px">TRAVEL SHOP <svg width="9" height="6" viewBox="0 0 9 6"><path d="M1 1l3.5 3.5L8 1" stroke="#fff" fill="none" stroke-width="1.4"/></svg></div>
    <div class="abs nav-link" style="left:1051px">CONTACT</div>
  </nav>
</header>

<section>
  <div class="abs hero" role="img" aria-label="Portrait of the site author smiling in front of a desert highway stretching toward red rock formations, washed over a golden vintage map"></div>
  <div class="abs hero-card">
    <h1>DREAMING OF SOLO TRAVEL?<br>TIRED OF NAYSAYERS?</h1>
    <span class="btn-ghost">READ MORE</span>
  </div>
  <div class="abs dots"><span class="on"></span><span></span><span></span></div>
</section>

<section class="abs intro">
  <h2>Hi, I'm Marta. I took my first solo trip at 15. I'll show you how to travel...</h2>
  <ul>
    <li><b>Smart</b>: practical tools to help you plan - and afford - the perfect trip</li>
    <li><b>Safe</b>: down-to-earth advice and a ton of safety recommendations</li>
    <li><b>Solo</b>: yes, you can do it!</li>
  </ul>
</section>

<div class="abs cta">Thinking of solo travel? <u>CLICK HERE</u> to find out how.</div>

<section>
  <div class="abs toolkit"></div>
  <h2 class="abs section-title" style="top:983px">TRAVEL TOOLKIT</h2>
  <div class="abs arrow" style="left:68px;top:1170px"><svg width="10" height="10" viewBox="0 0 10 10"><path d="M7 1L3 5l4 4" stroke="#fff" stroke-width="2" fill="none"/></svg></div>
  <div class="abs cards" style="top:1055px">
    <div class="card"><div class="card-head"><h3>Eating with locals</h3><p>The Ultimate guide to social dining</p></div><div class="card-photo" role="img" aria-label="Travellers sharing food with locals at a market" style="background:linear-gradient(#8a8276,#5d574e)"></div></div>
    <div class="card"><div class="card-head"><h3>Your packing list</h3><p>Take what you need-no more</p></div><div class="card-photo" role="img" aria-label="Travel gear laid out ready for packing" style="background:linear-gradient(#4a4658,#2c2a36)"></div></div>
    <div class="card"><div class="card-head"><h3>No single supplement</h3><p>17 Ways to Avoid Paying it</p></div><div class="card-photo" role="img" aria-label="Cruise ship lit in blue at night" style="background:linear-gradient(#1e3a66,#0d1526)"></div></div>
    <div class="card"><div class="card-head"><h3>Stress management course</h3><p>How to travel stress-free</p></div><div class="card-photo" role="img" aria-label="Assorted travel items spread on a table" style="background:linear-gradient(#8c8c86,#4e5052)"></div></div>
  </div>
  <div class="abs arrow" style="left:1106px;top:1170px"><svg width="10" height="10" viewBox="0 0 10 10"><path d="M3 1l4 4-4 4" stroke="#fff" stroke-width="2" fill="none"/></svg></div>
</section>

<section>
  <h2 class="abs section-title" style="top:1395px">DESTINATIONS</h2>
  <div class="abs cards" style="top:1469px">
    <div class="card"><div class="card-head"><h3>Solo in Argentina</h3><p>Does it really take two to tango?</p></div><div class="card-photo" role="img" aria-label="Quiet colonial street in Argentina" style="background:linear-gradient(#8a7a66,#5a4c3e)"></div><div class="card-link">CLICK HERE &gt;&gt;</div></div>
    <div class="card"><div class="card-head"><h3>Europe for foodies</h3><p>9 top destinations to try in October</p></div><div class="card-photo" role="img" aria-label="Plate of pastries" style="background:linear-gradient(#9a8a78,#6a5444)"></div><div class="card-link">CLICK HERE &gt;&gt;</div></div>
    <div class="card"><div class="card-head"><h3>Solo female travel</h3><p>A 3-week Central Asia Itinerary</p></div><div class="card-photo" role="img" aria-label="Central Asian landscape at dusk" style="background:linear-gradient(#4e5256,#33383a)"></div><div class="card-link">CLICK HERE &gt;&gt;</div></div>
    <div class="card"><div class="card-head"><h3>Rebellious Carouge</h3><p>Geneva's Alter Ego?</p></div><div class="card-photo" role="img" aria-label="Flower-lined old town street in Carouge" style="background:linear-gradient(#8a8a86,#5a5650)"></div><div class="card-link">CLICK HERE &gt;&gt;</div></div>
  </div>
</section>

<section>
  <div class="abs solo-bg"></div>
  <div class="abs solo-panel">
    <h2>SOLO TRAVEL</h2>
    <p>Solo travel for women means... more freedom to get off the bus when something catches your eye... being able to change your mind and your direction... being more open towards others... being more spontaneous... taking risks... fewer compromises... or just lying in bed or going for a massage if you feel like it without having to make excuses to anyone.</p>
    <span class="btn-outline">READ MORE</span>
  </div>
  <svg class="abs" style="left:414px;top:2010px" width="70" height="50" viewBox="0 0 70 50"><path d="M6 16c8 22 34 30 52 12" stroke="#333" stroke-width="3" fill="none"/><path d="M48 26l11 1-2-11" stroke="#333" stroke-width="3" fill="none"/></svg>
  <div class="abs solo-photo" role="img" aria-label="Three instant photos of a palm beach, a cactus and a red scooter, linked by a dashed travel route over a dim street scene"></div>
  <div class="abs solo-frame"></div>
</section>

<footer>
  <div class="abs footer"></div>
  <h4 class="abs foot-h" style="left:87px">GET IN TOUCH</h4>
  <div class="abs foot-brand"><span class="name">Ladies Far Afield</span><span class="tag">For women who travel smart, safe + solo</span></div>
  <h4 class="abs foot-h" style="left:87px;top:2413px">FOLLOW US</h4>
  <div class="abs socials"><span><i></i></span><span><i></i></span><span><i></i></span><span><i></i></span><span><i></i></span></div>

  <h4 class="abs foot-h" style="left:453px">QUICK LINKS</h4>
  <ul class="abs quick">
    <li>START HERE</li><li>ABOUT</li><li>TRAVEL RESOURCES</li><li>BLOG</li><li>TRAVEL SHOP</li><li>CONTACT</li>
  </ul>

  <h4 class="abs foot-h" style="left:705px">CONTACT FORM</h4>
  <div class="abs field" style="left:705px;top:2338px;width:196px;height:44px">Name</div>
  <div class="abs field" style="left:915px;top:2338px;width:198px;height:44px">E mail address</div>
  <div class="abs field" style="left:705px;top:2400px;width:408px;height:77px;align-items:flex-start;padding-top:12px">Comments</div>
  <div class="abs send">SEND</div>

  <div class="abs bottom">@copyright 2016 Ladies Far Afield.All Rights Reserved</div>
</footer>

</body>
</html>
```